International Petrochemical business needs a web design for Tessaro Desk system

We need a web design for a "Tessaro Desk" system for an international petrochemical company. The web site is used internally within the company. It is hosted by an internal department which provides government permit request service for other departments.

We would like to see designs of two pages using color light blue. (home page, internal page as attached).
Home Page:
1. Header has a background image and small animation. Header on home page can be taller than the header of the internal page.
2. Layout as attached.

Internal Page:
1. Header can use the same background image as the home page and can be shorter to utilize the page for content.
2. The blue icon behind every captions represent an icon. When user move mouse over this icon, it displays the caption in Thai language as a tooltip. This icon needs to be redesign.

The final design should communicate the followings:
- Excellent service provided system in terms of time and accurary
- Rapid growth of business via building petrochemical refinery plant

For Internal Page, the blue circle behind every captions represent an icon. When mouse over this icon, a tool tip showing the caption in Thai language is shown. Please also design this icon..

There are more feedbacks from customer as followed:

1. Banner should consists of 
    1.1 "Approved" stamp on paper
    1.2 An image of Garuda. It is used on every government documents in Thailand
    1.3 Image of petrochemical plant
2. Each menu item (Home, Permit, Search, etc) should have different colors. Drop down menu will use the same color as its parent menu item.
3. Overall tone of the web page should be light blue with background of the body the web page in white
4. "New Request" button should use green color with icon on it
5. Table header of each box in the body of the page should use dark blue background with text in white

Please kindly submit your revisions.
Thank you.

Reason: We get some late feedbacks from customers which was just updated to all designers.

• 1. Design for 1024x768 screen resolution
2. Use light blue theme
3. Background of header where the company logo is must have white background

```html
<!DOCTYPE html>
<html lang="en">
<head>
<meta charset="utf-8">
<title>Tessaro Desk – Home</title>
<link href="https://fonts.googleapis.com/css2?family=Ubuntu:wght@400;500;700&family=Mulish:wght@400;600;700&display=swap" rel="stylesheet">
<style>
  :root{
    --page-bg:#c3d1dd;
    --panel-bg:#ffffff;
    --nav-active:#5bc8f2;
    --nav-text:#3a3a3a;
    --title-blue:#1a5aa6;
    --head-blue:#2a7fd0;
    --head-dark:#1a4f8c;
    --link-blue:#10418c;
    --row-alt:#f3f5f7;
    --rule:#e2e6ea;
    --text:#333a40;
    --muted:#9aa3ab;
    --green-top:#7cc21e;
    --green-bot:#4c970c;
  }
  *{box-sizing:border-box;margin:0;padding:0}
  html,body{width:885px;height:1200px;overflow:hidden}
  body{background:var(--page-bg);font-family:"Mulish",sans-serif;color:var(--text);position:relative}

  .site-header{position:absolute;left:66px;top:0;width:754px;height:85px;background:#fff;box-shadow:0 1px 3px rgba(0,0,0,.12)}
  .brand{position:absolute;left:34px;top:33px;font-family:"Mulish",sans-serif;font-weight:600;font-size:16px;line-height:18px;color:var(--nav-text)}
  .main-nav{position:absolute;left:235px;top:0;height:85px;display:flex}
  .main-nav a{display:flex;align-items:center;height:85px;padding:0 12px;font-size:10px;font-weight:600;letter-spacing:.3px;color:var(--nav-text);text-decoration:none;text-transform:uppercase}
  .main-nav a.active{background:var(--nav-active);color:#fff;padding:0 14px}
  .follow{position:absolute;left:627px;top:15px}
  .follow-label{font-size:9.5px;font-weight:700;color:var(--title-blue);text-transform:uppercase}
  .follow-icons{display:flex;gap:6px;margin-top:8px}
  .follow-icons span{width:19px;height:19px;border-radius:3px}
  .ic-1{background:#7cc4ea}.ic-2{background:#f4a93a}.ic-3{background:#4a72b4}.ic-4{background:#3a3a3a}

  .hero{position:absolute;left:66px;top:85px;width:754px;height:330px;
    background:linear-gradient(180deg,#c8d4e0 0%,#9fb2c6 45%,#5f7b99 80%,#3d5675 100%)}
  .badge{position:absolute;top:21px;width:53px;height:53px;border-radius:50%;background:#dfe6ec;box-shadow:0 1px 3px rgba(0,0,0,.2)}
  .badge-1{left:18px}.badge-2{left:76px}

  .content{position:absolute;left:66px;top:415px;width:754px;height:737px;background:var(--panel-bg);box-shadow:0 1px 3px rgba(0,0,0,.15)}

  .block{position:absolute}
  .block-title{font-family:"Ubuntu",sans-serif;font-weight:400;font-size:18px;color:var(--title-blue);height:26px}
  .data-table{width:100%;border-collapse:collapse;table-layout:fixed;font-size:11px}
  .data-table thead th{background:var(--head-blue);color:#fff;font-weight:700;font-size:11px;height:32px;text-align:left;padding-left:22px;position:relative;white-space:nowrap}
  .data-table thead th:first-child::after{content:"";position:absolute;left:0;bottom:-4px;border-left:4px solid var(--head-dark);border-bottom:4px solid transparent}
  .data-table tbody td{height:28px;padding-left:22px;border-right:1px solid var(--rule);white-space:nowrap}
  .data-table tbody td:last-child{border-right:none}
  .data-table tbody tr:nth-child(odd) td{background:var(--row-alt)}
  .data-table td.num{color:var(--link-blue);font-size:11.5px}
  .data-table td.date{font-size:10px;vertical-align:top;padding-top:7px}
  .data-table td.link a{color:var(--link-blue);text-decoration:underline;font-size:10px}
  .data-table td.sm{font-size:10px}
  .data-table tbody tr.pager td{background:#fff;height:26px;text-align:center;color:var(--muted);font-size:9.5px;box-shadow:0 2px 2px rgba(0,0,0,.06)}
  .pager b{color:var(--link-blue);margin-right:4px}
  .pager span{margin-right:4px}
  .center td{text-align:center;padding-left:0}
  .center td:first-child{text-align:left;padding-left:22px}

  .new-request-btn{position:absolute;left:388px;top:470px;width:351px;height:70px;
    background:linear-gradient(180deg,var(--green-top),var(--green-bot));display:flex;align-items:center;padding-left:18px;gap:18px;text-decoration:none}
  .new-request-btn span{font-family:"Ubuntu",sans-serif;font-weight:700;font-size:34px;color:#fff;letter-spacing:.5px}

  .site-footer{position:absolute;left:81px;top:1168px;width:724px;display:flex;justify-content:space-between;font-size:9.5px;color:#1e2a33}
  .site-footer nav a{color:#1e2a33;text-decoration:none;margin-right:7px}
</style>
</head>
<body>

<header class="site-header">
  <div class="brand">Norvale Group</div>
  <nav class="main-nav">
    <a href="#" class="active">Home</a>
    <a href="#">Permits</a>
    <a href="#">Search</a>
    <a href="#">Report</a>
    <a href="#">Admin</a>
    <a href="#">Help</a>
  </nav>
  <div class="follow">
    <div class="follow-label">Follow us</div>
    <div class="follow-icons"><span class="ic-1"></span><span class="ic-2"></span><span class="ic-3"></span><span class="ic-4"></span></div>
  </div>
</header>

<section class="hero" role="img" aria-label="Petrochemical refinery towers with steam under a pale blue sky">
  <span class="badge badge-1" role="img" aria-label="Approved document badge"></span>
  <span class="badge badge-2" role="img" aria-label="Government emblem badge"></span>
</section>

<main class="content">
  <div class="block" style="left:14px;top:15px;width:356px">
    <h2 class="block-title">New Request</h2>
    <table class="data-table" style="margin-top:5px">
      <colgroup><col style="width:138px"><col style="width:108px"><col style="width:110px"></colgroup>
      <thead><tr><th>Request No</th><th>Request Date</th><th>Branch</th></tr></thead>
      <tbody class="center">
        <tr><td class="num">56-0003</td><td class="date">20-4-2013</td><td class="sm">GC 1</td></tr>
        <tr><td class="num">56-0004</td><td class="date">20-4-2013</td><td class="sm">GC 2</td></tr>
        <tr><td class="num">56-0005</td><td class="date">20-4-2013</td><td class="sm">GC 3</td></tr>
        <tr><td class="num">56-0006</td><td class="date">20-4-2013</td><td class="sm">GC 4</td></tr>
        <tr class="pager"><td colspan="3"><b>1</b><span>2</span><span>3</span><span>4</span></td></tr>
      </tbody>
    </table>
  </div>

  <div class="block" style="left:383px;top:15px;width:356px">
    <h2 class="block-title">My Working Request</h2>
    <table class="data-table" style="margin-top:5px">
      <colgroup><col style="width:122px"><col style="width:103px"><col style="width:131px"></colgroup>
      <thead><tr><th>Request No</th><th>Request Date</th><th>Status</th></tr></thead>
      <tbody>
        <tr><td class="num">56-0003</td><td class="date">20-4-2013</td><td class="sm" style="padding-left:13px">Waiting for process</td></tr>
        <tr><td class="num">56-0004</td><td class="date">20-4-2013</td><td class="sm" style="padding-left:13px">In Proress</td></tr>
        <tr><td class="num">56-0005</td><td class="date">20-4-2013</td><td class="sm" style="padding-left:13px">Incomplete Document</td></tr>
        <tr><td class="num">56-0006</td><td class="date">20-4-2013</td><td class="sm" style="padding-left:13px">Cancel Request</td></tr>
        <tr class="pager"><td colspan="3"><b>1</b><span>2</span><span>3</span><span>4</span></td></tr>
      </tbody>
    </table>
  </div>

  <div class="block" style="left:14px;top:227px;width:725px">
    <h2 class="block-title">Expiring Permits</h2>
    <table class="data-table" style="margin-top:3px">
      <colgroup><col style="width:138px"><col style="width:108px"><col style="width:134px"><col style="width:102px"><col style="width:126px"><col style="width:117px"></colgroup>
      <thead><tr><th>Permit No.</th><th>Expire Date</th><th>Permit Name</th><th>Branch</th><th style="padding-left:6px">Required Time (Day)</th><th>Due Date</th></tr></thead>
      <tbody class="center">
        <tr><td class="link"><a href="#">AB56007</a></td><td class="sm">20-4-2013</td><td class="link"><a href="#">Permit Name #10</a></td><td class="sm">GC 1</td><td class="sm">30</td><td class="sm">-40</td></tr>
        <tr><td class="link"><a href="#">BIO5502</a></td><td class="sm">21-4-2013</td><td class="link"><a href="#">Permit Name #20</a></td><td class="sm">GC 2</td><td class="sm">60</td><td class="sm">15</td></tr>
        <tr><td class="link"><a href="#">TS34821</a></td><td class="sm">22-4-2013</td><td class="link"><a href="#">Permit Name #30</a></td><td class="sm">GC 3</td><td class="sm">90</td><td class="sm">25</td></tr>
        <tr><td class="link"><a href="#">GD47515</a></td><td class="sm">23-4-2013</td><td class="link"><a href="#">Permit Name #40</a></td><td class="sm">GC 4</td><td class="sm">120</td><td class="sm">-90</td></tr>
        <tr class="pager"><td colspan="6" style="text-align:left;padding-left:160px"><b>1</b><span>2</span><span>3</span><span>4</span></td></tr>
      </tbody>
    </table>
  </div>

  <div class="block" style="left:14px;top:443px;width:356px">
    <h2 class="block-title">My in Progress Requests</h2>
    <table class="data-table" style="margin-top:1px">
      <colgroup><col style="width:123px"><col style="width:102px"><col style="width:131px"></colgroup>
      <thead><tr><th style="padding-left:16px">Request No</th><th>Request Date</th><th>Status</th></tr></thead>
      <tbody>
        <tr><td class="num">56-0003</td><td class="date">20-4-2013</td><td class="sm" style="padding-left:13px">Waiting for process</td></tr>
        <tr><td class="num">56-0004</td><td class="date">20-4-2013</td><td class="sm" style="padding-left:13px">In Proress</td></tr>
        <tr><td class="num">56-0005</td><td class="date">20-4-2013</td><td class="sm" style="padding-left:13px">Incomplete Document</td></tr>
        <tr><td class="num">56-0006</td><td class="date">20-4-2013</td><td class="sm" style="padding-left:13px">Cancel Request</td></tr>
        <tr><td class="num">56-0003</td><td class="date">20-4-2013</td><td class="sm" style="padding-left:13px">Waiting for process</td></tr>
        <tr><td class="num">56-0004</td><td class="date">20-4-2013</td><td class="sm" style="padding-left:13px">In Proress</td></tr>
        <tr><td class="num">56-0005</td><td class="date">20-4-2013</td><td class="sm" style="padding-left:13px">Incomplete Document</td></tr>
        <tr class="pager"><td colspan="3"><b>1</b><span>2</span><span>3</span><span>4</span></td></tr>
      </tbody>
    </table>
  </div>

  <a href="#" class="new-request-btn">
    <svg width="60" height="50" viewBox="0 0 60 50" fill="none" stroke="#fff" stroke-width="3" stroke-linejoin="round" stroke-linecap="round" aria-hidden="true">
      <path d="M6 22 h40 v24 h-40 z"/>
      <path d="M12 30 h18 M12 37 h26"/>
      <path d="M24 28 l22 -22 l7 7 l-22 22 l-9 2 z"/>
      <path d="M42 10 l7 7"/>
    </svg>
    <span>NEW REQUEST</span>
  </a>

  <div class="block" style="left:388px;top:556px;width:351px">
    <h2 class="block-title">Recent Completed Requests</h2>
    <table class="data-table" style="margin-top:2px">
      <colgroup><col style="width:175px"><col style="width:176px"></colgroup>
      <thead><tr><th style="padding-left:20px">Request No</th><th style="padding-left:42px">Request Date</th></tr></thead>
      <tbody>
        <tr><td class="num" style="padding-left:19px">56-0003</td><td class="date" style="padding-left:65px">20-4-2013</td></tr>
        <tr><td class="num" style="padding-left:19px">56-0004</td><td class="date" style="padding-left:65px">20-4-2013</td></tr>
        <tr><td class="num" style="padding-left:19px">56-0005</td><td class="date" style="padding-left:65px">20-4-2013</td></tr>
        <tr class="pager"><td colspan="2"><b>1</b><span>2</span><span>3</span><span>4</span></td></tr>
      </tbody>
    </table>
  </div>
</main>

<footer class="site-footer">
  <nav><a href="#">Home</a><a href="#">Permits</a><a href="#">Search</a><a href="#">Report</a><a href="#">Admin</a><a href="#">Help</a></nav>
  <div>© Copyrights 2013 All rights Reserved</div>
</footer>

</body>
</html>
```